***Rustic Website Design - More design needed after!***

Tindlebrook Creative Agency
https://www.picturelane.example/tindlebrookco/

Website pages:
Home
About
Design
-Logo Design and Branding
-Graphic Design
Websites
-Hosting, Maintenance and Support
Social Media
Managed Marketing
Portfolio
Contact

I have included a link to our Picturelane so you get a feel as to how we want to be.

We want to be approachable to new and rural businesses. - Colours included as image

Target Market(s)

Start Up Businesses & Rural Businesses

Number of Pages Required

2 page

Font styles to use
Serif
Other font styles liked:
• Barnyard, Rustic

Requirements
Must have
• Menu, Social Media Icons, rustic lines like our social media.

```html
<!DOCTYPE html>
<html lang="en">
<head>
<meta charset="utf-8">
<title>Tindlebrook Creative – Your Rural Business's Marketing Department</title>
<link href="https://fonts.googleapis.com/css2?family=Amarante&family=Caveat+Brush&family=Allura&display=swap" rel="stylesheet">
<style>
:root{
  --green:#0f4b43;
  --green-dark:#0b3c35;
  --yellow:#f5c400;
  --ink:#111111;
  --text:#555555;
  --white:#ffffff;
  --footer:#070707;
  --footer-text:#9a9a9a;
}
*{margin:0;padding:0;box-sizing:border-box}
html,body{width:1200px;height:3722px;overflow:hidden;background:var(--white)}
body{font-family:"Amarante",Georgia,serif;color:var(--ink)}
.page{position:relative;width:1200px;height:3722px;overflow:hidden}
.abs{position:absolute}
a{color:inherit;text-decoration:none}

/* header + hero */
.hero{left:0;top:0;width:1200px;height:670px;background:linear-gradient(160deg,#135247 0%,var(--green) 55%,var(--green-dark) 100%)}
.brand{left:86px;top:22px;color:var(--white);font-size:26px;line-height:1}
.brand .dot{display:inline-block;width:12px;height:12px;border-radius:50%;background:var(--yellow);margin-right:8px;vertical-align:middle}
.nav{right:80px;top:44px;display:flex;gap:20px;font-size:12.5px;color:var(--white)}
.nav .active{color:var(--yellow);position:relative}
.nav .active::after{content:"";position:absolute;left:-12px;right:-12px;top:47px;height:2px;background:var(--yellow)}
.nav-rule{left:0;top:94px;width:1200px;height:1px;background:rgba(255,255,255,.12)}
.hero-title{left:82px;top:130px;font-family:"Allura",cursive;color:var(--white);line-height:.95}
.hero-title .l1{font-size:118px;display:block}
.hero-title .l1 span{color:var(--yellow)}
.hero-title .l2{font-size:140px;display:block;margin-left:10px}
.hero-sub{left:107px;top:452px;color:var(--white);font-size:21px;line-height:1.6;width:340px}
.hero-art{left:470px;top:150px;width:680px;height:460px;border-radius:40%;background:radial-gradient(ellipse at 55% 45%,#e9e9e9 0%,#c43f7f 30%,#2f7fb0 55%,rgba(15,75,67,0) 72%)}
.edge{left:0;width:1200px}

/* intro */
.intro-head{left:150px;top:740px;width:900px;text-align:center;font-size:26px;line-height:1.6}
.intro-text{left:108px;top:860px;width:984px;text-align:center;font-size:14px;line-height:2.05;color:var(--text)}
.divider{left:96px;top:1040px;width:1004px;height:1px;background:#ececec}

/* feature sections */
.sec-title{font-family:"Caveat Brush",cursive;font-size:68px;line-height:1.1;color:var(--ink)}
.sec-text{font-size:14.5px;line-height:2;color:var(--text)}
.art-box{border-radius:30px}
.card{position:absolute;background:var(--white);border-radius:12px;display:flex;align-items:center;padding-left:30px;font-size:28px;color:var(--ink)}
.card .ic{width:66px;height:66px;border-radius:50%;background:var(--green);display:flex;align-items:center;justify-content:center;margin-right:28px;flex:none}

/* services band */
.band{left:0;top:1800px;width:1200px;height:700px;background:var(--green)}
.band-title{left:0;top:1940px;width:1200px;text-align:center;color:var(--white);font-size:42px}
.svc{position:absolute;top:2104px;width:240px;height:272px;background:var(--white);border-radius:8px;text-align:center;padding-top:110px}
.svc h3{font-weight:400;font-size:24px;line-height:1.3;padding:0 20px}
.svc p{font-size:14px;line-height:2;color:var(--text);margin-top:18px;padding:0 28px}
.svc-badge{position:absolute;left:62px;top:-58px;width:116px;height:116px;border-radius:50%;background:var(--green);border:6px solid var(--yellow);display:flex;align-items:center;justify-content:center}

/* footer */
.footer{left:0;top:3250px;width:1200px;height:472px;background:var(--footer)}
.f-brand{left:116px;top:3348px;color:var(--white);font-size:26px}
.f-brand .dot{display:inline-block;width:12px;height:12px;border-radius:50%;background:var(--yellow);margin-right:8px;vertical-align:middle}
.f-about{left:119px;top:3420px;width:240px;font-size:13px;line-height:1.75;color:var(--footer-text)}
.f-social{left:119px;top:3520px;display:flex;gap:14px;font-size:12px;color:var(--yellow)}
.f-head{color:var(--white);font-size:16px}
.f-list{list-style:none;font-size:13px;color:var(--footer-text)}
.f-list li{height:31px;padding-left:26px;position:relative}
.f-list li::before{content:"→";position:absolute;left:0;top:-2px;color:var(--yellow)}
.f-contact{font-size:13px;line-height:1.6;color:var(--footer-text)}
.f-contact .row{position:relative;padding-left:22px;margin-bottom:12px}
.f-contact svg{position:absolute;left:0;top:3px}
.f-contact .mail{color:var(--yellow)}
.f-rule{left:60px;top:3643px;width:1080px;height:1px;background:#2a2a2a}
.copy{left:0;top:3672px;width:1200px;text-align:center;font-size:12px;color:var(--footer-text)}
.copy b{color:var(--white);font-weight:400}
</style>
</head>
<body>
<div class="page">

  <!-- Hero -->
  <div class="abs hero"></div>
  <div class="abs hero-art" role="img" aria-label="Illustration of a computer monitor with graphic design tools and colourful paint splashes"></div>
  <a class="abs brand" href="#"><span class="dot"></span>Tindlebrook Creative</a>
  <nav class="abs nav">
    <a class="active" href="#">Home</a><a href="#">About</a><a href="#">Design</a><a href="#">Websites</a><a href="#">Social Media</a><a href="#">Managed Marketing</a><a href="#">Portfolio</a><a href="#">Contact</a>
  </nav>
  <div class="abs nav-rule"></div>
  <h1 class="abs hero-title"><span class="l1"><span>Creative</span> Initiative</span><span class="l2">Marketing</span></h1>
  <p class="abs hero-sub">Your Rural Business's Marketing Department</p>
  <svg class="abs edge" style="top:612px" width="1200" height="60" viewBox="0 0 1200 60" preserveAspectRatio="none">
    <path fill="#ffffff" d="M0,36 L18,22 L34,40 L52,18 L70,34 L88,14 L104,30 L122,20 L140,38 L158,12 L176,32 L194,24 L212,40 L230,16 L248,30 L266,22 L284,36 L302,10 L320,28 L338,20 L356,38 L374,14 L392,32 L410,22 L428,40 L446,18 L464,30 L482,12 L500,34 L518,22 L536,38 L554,16 L572,30 L590,20 L608,36 L626,12 L644,28 L662,22 L680,40 L698,16 L716,32 L734,20 L752,38 L770,14 L788,30 L806,24 L824,40 L842,18 L860,32 L878,12 L896,30 L914,22 L932,38 L950,16 L968,34 L986,20 L1004,36 L1022,12 L1040,30 L1058,22 L1076,40 L1094,18 L1112,32 L1130,14 L1148,34 L1166,20 L1184,36 L1200,22 L1200,60 L0,60 Z"/>
  </svg>

  <!-- Intro -->
  <h2 class="abs intro-head" style="font-weight:400">We believe in prosperity, empowerment and opportunity for rural local businesses in and around Somerset.</h2>
  <p class="abs intro-text">We help these businesses thrive by creating customised designs, websites and marketing strategies. We reduce their time investment, we remove the need for specialised knowledge and hours of self-learning, this avoids the frustration and disappointment that do-it-yourself options can bring. Our years of experience and local rural understanding makes the process simple, friendly and effective.</p>
  <div class="abs divider"></div>

  <!-- Logo & Graphic Design -->
  <h2 class="abs sec-title" style="left:90px;top:1118px;font-weight:400">Logo &amp; Graphic<br>Design</h2>
  <p class="abs sec-text" style="left:94px;top:1295px;width:340px">We strive to capture the heart and soul of your business into your brand.</p>
  <div class="abs art-box" style="left:80px;top:1370px;width:460px;height:340px;background:radial-gradient(ellipse at 50% 55%,#7fc241 0%,#3aa0d9 35%,#e4e4e4 62%,rgba(255,255,255,0) 75%)" role="img" aria-label="Illustration of 3D graphic design lettering, paint tubes and a logo design splash"></div>
  <svg class="abs" style="left:572px;top:1132px" width="572" height="600" viewBox="0 0 572 600">
    <path fill="#f5c400" d="M22,28 L60,14 L110,22 L160,8 L220,18 L280,6 L340,20 L400,10 L460,22 L520,12 L556,30 L548,80 L566,140 L552,200 L568,260 L550,320 L566,380 L552,440 L564,500 L548,560 L520,588 L460,578 L400,592 L340,580 L280,594 L220,582 L160,596 L100,584 L50,594 L14,570 L22,510 L6,450 L20,390 L4,330 L18,270 L2,210 L16,150 L4,90 Z"/>
  </svg>
  <div class="card" style="left:625px;top:1205px;width:468px;height:98px"><span class="ic"><svg width="30" height="30" viewBox="0 0 30 30" fill="none" stroke="#fff" stroke-width="2.2"><rect x="8" y="6" width="14" height="20" rx="7"/><line x1="15" y1="6" x2="15" y2="13"/></svg></span>Capture the heart and soul</div>
  <div class="card" style="left:625px;top:1327px;width:468px;height:98px"><span class="ic"><svg width="30" height="30" viewBox="0 0 30 30" fill="none" stroke="#fff" stroke-width="2.2"><path d="M6,24 L10,16 L21,5 L25,9 L14,20 Z"/><line x1="17" y1="9" x2="21" y2="13"/></svg></span>Business into your brand</div>
  <div class="card" style="left:625px;top:1450px;width:468px;height:98px"><span class="ic"><svg width="30" height="30" viewBox="0 0 30 30" fill="none" stroke="#fff" stroke-width="2.2"><path d="M15,27 L8,14 L15,6 L22,14 Z"/><circle cx="15" cy="15" r="2"/><line x1="15" y1="6" x2="15" y2="2"/></svg></span>Unique brand</div>
  <div class="card" style="left:625px;top:1572px;width:468px;height:98px"><span class="ic"><svg width="30" height="30" viewBox="0 0 30 30" fill="none" stroke="#fff" stroke-width="2.2"><circle cx="15" cy="7" r="3"/><line x1="13" y1="10" x2="7" y2="26"/><line x1="17" y1="10" x2="23" y2="26"/><line x1="10" y1="19" x2="20" y2="19"/></svg></span>Explain what you believe</div>

  <!-- Services band -->
  <div class="abs band"></div>
  <svg class="abs edge" style="top:1795px" width="1200" height="60" viewBox="0 0 1200 60" preserveAspectRatio="none">
    <path fill="#ffffff" d="M0,0 L1200,0 L1200,24 L1182,38 L1164,20 L1146,42 L1128,26 L1110,44 L1092,22 L1074,36 L1056,18 L1038,40 L1020,28 L1002,46 L984,22 L966,38 L948,20 L930,42 L912,26 L894,44 L876,18 L858,36 L840,24 L822,42 L804,20 L786,38 L768,26 L750,46 L732,22 L714,36 L696,18 L678,40 L660,28 L642,44 L624,20 L606,38 L588,24 L570,42 L552,18 L534,36 L516,26 L498,44 L480,22 L462,38 L444,20 L426,40 L408,28 L390,46 L372,22 L354,36 L336,18 L318,42 L300,26 L282,44 L264,20 L246,38 L228,24 L210,42 L192,18 L174,36 L156,26 L138,44 L120,22 L102,38 L84,20 L66,40 L48,28 L30,44 L12,22 L0,34 Z"/>
  </svg>
  <h2 class="abs band-title" style="font-weight:400">All your marketing under one roof</h2>

  <div class="svc" style="left:87px">
    <div class="svc-badge"><svg width="44" height="44" viewBox="0 0 44 44" fill="none" stroke="#fff" stroke-width="2.4"><path d="M22,38 L14,24 L22,14 L30,24 Z"/><circle cx="22" cy="24" r="2.5"/><path d="M6,16 Q22,4 38,16"/><rect x="3" y="13" width="6" height="6"/><rect x="35" y="13" width="6" height="6"/></svg></div>
    <h3>Logo &amp; Graphic Design</h3><p>We strive to capture the heart and soul</p>
  </div>
  <div class="svc" style="left:350px">
    <div class="svc-badge" style="background:var(--yellow);border-color:var(--green)"><svg width="48" height="44" viewBox="0 0 48 44" fill="none" stroke="#0f4b43" stroke-width="2.4"><rect x="16" y="14" width="28" height="18" rx="2"/><line x1="30" y1="32" x2="30" y2="38"/><line x1="22" y1="38" x2="38" y2="38"/><rect x="4" y="22" width="8" height="16"/><path d="M8,22 L8,10 L18,6"/></svg></div>
    <h3>Websites</h3><p>We produce awesome affordable Pressfold websites.</p>
  </div>
  <div class="svc" style="left:614px">
    <div class="svc-badge"><svg width="44" height="44" viewBox="0 0 44 44" fill="none" stroke="#fff" stroke-width="2.4"><rect x="8" y="10" width="26" height="28" rx="2"/><path d="M12,10 L12,6 L24,6 L27,10"/><circle cx="21" cy="26" r="5"/><line x1="14" y1="34" x2="28" y2="34"/></svg></div>
    <h3>Website Management</h3><p>Take the stress out of your website management – we'll keep your website</p>
  </div>
  <div class="svc" style="left:878px">
    <div class="svc-badge"><svg width="44" height="44" viewBox="0 0 44 44" fill="none" stroke="#fff" stroke-width="2.4"><circle cx="22" cy="12" r="6"/><line x1="22" y1="2" x2="22" y2="4"/><line x1="12" y1="6" x2="14" y2="8"/><line x1="32" y1="6" x2="30" y2="8"/><path d="M8,24 L22,18 L36,24 L22,30 Z"/><path d="M8,24 L8,34 L22,40 L36,34 L36,24"/></svg></div>
    <h3>Social Media</h3><p>Whether you just dont know where to start with social media, or you</p>
  </div>

  <svg class="abs edge" style="top:2460px" width="1200" height="60" viewBox="0 0 1200 60" preserveAspectRatio="none">
    <path fill="#ffffff" d="M0,34 L18,20 L36,40 L54,16 L72,32 L90,22 L108,42 L126,14 L144,30 L162,24 L180,40 L198,12 L216,34 L234,20 L252,38 L270,18 L288,32 L306,10 L324,30 L342,22 L360,40 L378,16 L396,32 L414,22 L432,38 L450,12 L468,30 L486,20 L504,40 L522,14 L540,32 L558,24 L576,42 L594,16 L612,30 L630,20 L648,38 L666,12 L684,32 L702,22 L720,40 L738,18 L756,30 L774,14 L792,36 L810,22 L828,40 L846,16 L864,30 L882,24 L900,42 L918,14 L936,32 L954,20 L972,38 L990,12 L1008,30 L1026,22 L1044,40 L1062,18 L1080,34 L1098,14 L1116,32 L1134,22 L1152,40 L1170,16 L1188,30 L1200,24 L1200,60 L0,60 Z"/>
  </svg>

  <!-- Websites -->
  <svg class="abs" style="left:44px;top:2608px" width="572" height="540" viewBox="0 0 572 540">
    <path fill="#f5c400" d="M20,24 L70,12 L130,22 L190,6 L250,18 L310,8 L370,20 L430,6 L490,18 L550,14 L556,70 L568,130 L552,190 L566,250 L550,310 L564,370 L552,430 L566,490 L540,528 L480,516 L420,532 L360,518 L300,534 L240,520 L180,534 L120,520 L60,532 L16,514 L24,450 L8,390 L22,330 L6,270 L20,210 L4,150 L18,90 Z"/>
  </svg>
  <div class="card" style="left:98px;top:2705px;width:468px;height:98px"><span class="ic"><svg width="30" height="30" viewBox="0 0 30 30" fill="none" stroke="#fff" stroke-width="2.2"><rect x="4" y="9" width="22" height="15" rx="2"/><path d="M11,9 L11,6 L19,6 L19,9"/><line x1="4" y1="15" x2="26" y2="15"/></svg></span>Capture the heart and soul</div>
  <div class="card" style="left:98px;top:2828px;width:468px;height:98px"><span class="ic"><svg width="30" height="30" viewBox="0 0 30 30" fill="none" stroke="#fff" stroke-width="2.2"><rect x="4" y="5" width="22" height="20" rx="2"/><line x1="4" y1="11" x2="26" y2="11"/><line x1="9" y1="16" x2="21" y2="16"/><line x1="9" y1="20" x2="21" y2="20"/></svg></span>Business into your brand</div>
  <div class="card" style="left:98px;top:2950px;width:468px;height:98px"><span class="ic"><svg width="30" height="30" viewBox="0 0 30 30" fill="none" stroke="#fff" stroke-width="2.2"><rect x="4" y="6" width="22" height="16" rx="2"/><line x1="11" y1="26" x2="19" y2="26"/><path d="M9,18 Q15,10 21,18"/></svg></span>Unique brand</div>
  <h2 class="abs sec-title" style="left:685px;top:2645px;font-weight:400;font-size:76px">Websites</h2>
  <p class="abs sec-text" style="left:699px;top:2757px;width:410px">We strive to capture the heart and soul of your business into your brand. The result is not only a unique brand but a tool for you to explain what you believe in.</p>
  <div class="abs" style="left:670px;top:2880px;width:456px;height:245px;background:linear-gradient(90deg,#d9dde3 0%,#f2f2f2 30%,#2e2e2e 50%,#eef0f2 70%,#d7dbe0 100%);border-radius:6px" role="img" aria-label="Row of website page layouts shown in perspective"></div>

  <!-- Footer -->
  <div class="abs footer"></div>
  <svg class="abs edge" style="top:3210px" width="1200" height="50" viewBox="0 0 1200 50" preserveAspectRatio="none">
    <path fill="#070707" d="M0,24 L20,14 L40,30 L60,8 L80,26 L100,16 L120,34 L140,10 L160,28 L180,18 L200,36 L220,12 L240,26 L260,6 L280,30 L300,18 L320,34 L340,12 L360,28 L380,20 L400,38 L420,10 L440,26 L460,16 L480,32 L500,8 L520,28 L540,18 L560,36 L580,12 L600,26 L620,20 L640,38 L660,10 L680,30 L700,16 L720,34 L740,8 L760,28 L780,18 L800,36 L820,12 L840,26 L860,18 L880,34 L900,10 L920,28 L940,16 L960,36 L980,12 L1000,26 L1020,20 L1040,38 L1060,8 L1080,30 L1100,16 L1120,34 L1140,12 L1160,28 L1180,18 L1200,30 L1200,50 L0,50 Z"/>
  </svg>
  <a class="abs f-brand" href="#"><span class="dot"></span>Tindlebrook Creative</a>
  <p class="abs f-about">We strive to capture the heart and soul of your business into your brand. The result is not only a unique</p>
  <div class="abs f-social"><a href="#">Chirpwire</a><a href="#">Friendvine</a><a href="https://www.picturelane.example/tindlebrookco/">Picturelane</a><a href="#">Workweave</a></div>

  <h4 class="abs f-head" style="left:405px;top:3352px;font-weight:400">Quick Links</h4>
  <ul class="abs f-list" style="left:408px;top:3404px">
    <li>Home</li><li>About</li><li>Design</li><li>Logo Design and Branding</li><li>Graphic Design</li>
  </ul>
  <ul class="abs f-list" style="left:625px;top:3404px">
    <li>Websites</li><li>Hosting, Maintenance and Support</li><li>Social Media</li><li>Managed Marketing</li><li>Portfolio</li><li>Contact</li>
  </ul>

  <h4 class="abs f-head" style="left:878px;top:3352px;font-weight:400">Contact</h4>
  <div class="abs f-contact" style="left:878px;top:3400px;width:200px">
    <div class="row"><svg width="12" height="14" viewBox="0 0 12 14"><path fill="#f5c400" d="M6,0 A5,5 0 0 1 11,5 C11,9 6,14 6,14 C6,14 1,9 1,5 A5,5 0 0 1 6,0 Z"/><circle cx="6" cy="5" r="2" fill="#070707"/></svg>Ashcombe, Wendlebury, Somerset</div>
    <div class="row" style="margin-bottom:2px"><svg width="12" height="10" viewBox="0 0 12 10"><rect x="0" y="0" width="12" height="10" fill="#f5c400"/><path d="M0,0 L6,5 L12,0" stroke="#070707" fill="none"/></svg><span class="mail">hello@tindlebrook.example</span></div>
    <div class="row"><svg width="12" height="12" viewBox="0 0 12 12"><path fill="#f5c400" d="M2,0 L5,3 L3.5,5 Q5,8 7,8.5 L9,7 L12,10 L10,12 Q3,11 0,2 Z"/></svg>+44 (0) 1632 960418</div>
  </div>

  <div class="abs f-rule"></div>
  <p class="abs copy">© 2021 <b>Tindlebrook Creative.</b> All rights reserved.</p>
</div>
</body>
</html>
```